Pelvin Advisory Business Card Design

Business card for business consulting company, using attached logo. We do financial and strategic consulting, and want a clean, professional image with a bit of fun. Our logo is a flat whale tail, which symbolizes the Orca whale, a highly collaborative, group based animal that is very successful in navigating the ocean, protecting the herd, and hunting. We like the logo that is blue and gray on white one one side, but would be open to a blue card with white lettering on the other side... or whatever you'd suggest
Updates
Hi all - I have had the logo modified to take the shadowing off the tail. I will post it on the brief... under a file name called updated logo. thank you Added Saturday, April 25, 2015
Target Market(s)
Small to medium sized businesses ($10M to $500M in revenue per year), financial and sales executives, general managers, attorneys and CPAs
Industry/Entity Type
Financial
Contact Information for Business Card
Want company name, contact info - name, title, telephone, email, website, linkedin, twitter and Facebook. No physical address yet.
Requirements
Must have
- contemporary design, bold, strong, confident but with a bit of fun. prominently feature the logo and the whale tail icon
Nice to have
- unique touches that would differentiate us from a regular card... for example, logo and writing all on front on white background, but on back - logo in white on a blue background
- open to idea of different shapes of card than standard... but not sure

```html
<!DOCTYPE html>
<html lang="en">
<head>
<meta charset="utf-8">
<title>Pelvin Advisory – Business Card</title>
<link href="https://fonts.googleapis.com/css2?family=Open+Sans:wght@400;600;700&display=swap" rel="stylesheet">
<style>
  :root {
    --navy: #0b3b6e;
    --navy-deep: #083262;
    --grey: #8a8f96;
    --ink: #2c2f33;
    --white: #ffffff;
    --stage: #e9eaec;
  }
  * { box-sizing: border-box; margin: 0; padding: 0; }
  html, body { width: 1200px; height: 873px; overflow: hidden; }
  body {
    background: var(--stage);
    font-family: "Open Sans", Arial, sans-serif;
    display: flex;
    align-items: center;
    justify-content: center;
    gap: 60px;
  }
  .card {
    position: relative;
    width: 500px;
    height: 286px;
    overflow: hidden;
    box-shadow: 0 6px 18px rgba(0,0,0,0.12);
  }

  /* Wordmark */
  .brand { display: flex; flex-direction: column; align-items: flex-end; width: max-content; }
  .brand-row { display: flex; align-items: center; gap: 8px; }
  .brand-mark { width: 30px; height: 30px; border-radius: 5px; }
  .brand-name { font-weight: 600; font-size: 31px; letter-spacing: -0.5px; line-height: 1; }
  .brand-tag { font-size: 9px; letter-spacing: 0.4px; margin-top: 2px; }

  /* Front */
  .card-front { background: var(--white); }
  .card-front .brand { position: absolute; left: 28px; top: 30px; }
  .card-front .brand-mark { background: var(--navy); }
  .card-front .brand-name { color: var(--navy); }
  .card-front .brand-tag { color: var(--navy); }

  .contact {
    position: absolute; left: 28px; bottom: 28px;
    font-size: 10.5px; line-height: 15px; color: var(--ink);
    list-style: none;
  }
  .contact li { display: flex; align-items: center; gap: 6px; }
  .contact .icon { width: 10px; height: 10px; flex: none; }
  .contact .plain { padding-left: 0; }

  .name-bar {
    position: absolute; right: 0; top: 128px;
    width: 250px; height: 52px;
    background: var(--navy);
    border-radius: 5px 0 0 5px;
    color: var(--white);
    display: flex; flex-direction: column; justify-content: center;
    padding-left: 22px;
  }
  .name-bar .person { font-weight: 700; font-size: 13px; letter-spacing: 1px; }
  .name-bar .role { font-size: 11px; }

  .social {
    position: absolute; left: 250px; bottom: 30px;
    display: flex; gap: 9px; list-style: none;
  }
  .social li { width: 13px; height: 13px; background: var(--navy); border-radius: 2px; }

  /* Back */
  .card-back { background: var(--navy); }
  .card-back .brand { position: absolute; left: 50%; top: 96px; transform: translateX(-50%); }
  .card-back .brand-mark { background: var(--white); }
  .card-back .brand-name { color: var(--white); font-size: 36px; }
  .card-back .brand-tag { color: var(--white); }
  .website {
    position: absolute; left: 26px; bottom: 24px;
    color: var(--white); font-size: 9px; letter-spacing: 2.5px;
  }
</style>
</head>
<body>

  <section class="card card-front" aria-label="Card front">
    <div class="brand">
      <div class="brand-row">
        <span class="brand-mark"></span>
        <span class="brand-name">Pelvin Advisory</span>
      </div>
      <span class="brand-tag">business consulting</span>
    </div>

    <ul class="contact">
      <li class="plain">1180 North Alder Lane</li>
      <li class="plain">Tempe, AZ 85281</li>
      <li>
        <svg class="icon" viewBox="0 0 10 10"><rect width="10" height="10" rx="1.5" fill="#0b3b6e"/><path d="M3 2.4h1.2l.5 1.6-.8.6a4 4 0 0 0 1.6 1.6l.6-.8 1.6.5v1.2A.6.6 0 0 1 7.1 8 5.2 5.2 0 0 1 2 2.9a.6.6 0 0 1 1-.5z" fill="#fff"/></svg>
        5550142270
      </li>
      <li>
        <svg class="icon" viewBox="0 0 10 10"><rect width="10" height="10" rx="1.5" fill="#0b3b6e"/><rect x="3" y="1.8" width="4" height="6.4" rx="0.8" fill="#fff"/></svg>
        5550142270
      </li>
      <li>
        <svg class="icon" viewBox="0 0 10 10"><rect width="10" height="10" rx="1.5" fill="#0b3b6e"/><rect x="2" y="3" width="6" height="4.2" fill="#fff"/><path d="M2 3l3 2.3L8 3" stroke="#0b3b6e" stroke-width="0.7" fill="none"/></svg>
        dana@pelvinadvisory.com
      </li>
    </ul>

    <div class="name-bar">
      <span class="person">DANA WHITLOW</span>
      <span class="role">Manager</span>
    </div>

    <ul class="social" aria-label="Social profiles">
      <li></li><li></li><li></li>
    </ul>
  </section>

  <section class="card card-back" aria-label="Card back">
    <div class="brand">
      <div class="brand-row">
        <span class="brand-mark"></span>
        <span class="brand-name">Pelvin Advisory</span>
      </div>
      <span class="brand-tag">business consulting</span>
    </div>
    <span class="website">www.pelvinadvisory.com</span>
  </section>

</body>
</html>
```